Business Card Design - Construction Company

Tarrowin Construction is in need of a sharp, modern business card design that has an architectural/high fashion feel.

We are looking for a two sided card.

One side simple dark grey/black with some texture in the background. e.g. (a mosaic of simple interconnecting shapes or a shadow of the logo.) Something to draw attention and create interest.It will need to feature a large Tarrowin construction logo (files attached) in metallic gradient or plain white.

The other side should contain all of our information:

(in largest text)
Name of person
Tarrowin Construction Pty. Ltd.

Licensed builders specialising in:
- Bathrooms
- Kitchens
- Commercial interiors

(mid sized text)
Phone number
Fax number
person@tarrowinconstruction.example.au
www. tarrowinconstruction.example.au

(smaller text)
ABN: 62407938215
BSA license: xxx-xxxx
PO Box 8641 Kellsmoor QLD 4019 (address)

Target Market(s)

professional home and business owners

Industry/Entity Type

Construction

Requirements
Must have
• Must be bold, professional looking and modern.
Nice to have
• We are undecided as to what kind of printing we will go with.
Definitely square edged.
Probably high quality satin card.
We are also interested in designs that would work well on transparent or translucent plastic.
Ideally we would print two versions.
Should not have
• Nothing with an antique feel.
No wild colours. Small amounts of colour can be good in the right place.

```html
<!DOCTYPE html>
<html lang="en">
<head>
<meta charset="utf-8">
<title>Tarrowin Construction – Business Cards</title>
<link rel="stylesheet" href="https://fonts.googleapis.com/css2?family=Arimo:wght@400;700&display=swap">
<style>
  :root {
    --stage: #3b3b3d;
    --card-navy: #07101f;
    --band-light: #e9f6fc;
    --band-mid: #58b6e4;
    --band-deep: #0b2a4c;
    --ink-white: #ffffff;
    --ink-grey: #6d7684;
    --ink-logo: #0c3a63;
    --silver: #c9ced5;
    --pattern-a: #0d2a52;
    --pattern-b: #07152c;
  }
  * { box-sizing: border-box; margin: 0; padding: 0; }
  html, body { width: 1200px; height: 900px; overflow: hidden; }
  body {
    position: relative;
    background: var(--stage);
    font-family: "Arimo", Arial, sans-serif;
    color: var(--ink-white);
  }
  .card {
    position: absolute;
    background: var(--card-navy);
    overflow: hidden;
  }
  .card--front-a { left: 12px; top: 45px; width: 584px; height: 327px; }
  .card--front-b { left: 605px; top: 45px; width: 583px; height: 327px; }
  .card--back { left: 248px; top: 468px; width: 627px; height: 350px; }

  /* shared pieces */
  .holder-name { position: absolute; font-weight: 700; white-space: nowrap; }
  .wordmark {
    position: absolute;
    display: flex; align-items: center; justify-content: center; gap: 6px;
    font-weight: 700; color: var(--ink-logo); white-space: nowrap; letter-spacing: 1px;
  }
  .wordmark__dot { width: 14px; height: 14px; border-radius: 50%; background: var(--ink-logo); }
  .licence-intro { position: absolute; color: var(--ink-grey); font-size: 12px; white-space: nowrap; }
  .service { position: absolute; font-weight: 700; font-size: 14px; white-space: nowrap; }
  .footnote { position: absolute; bottom: 8px; font-size: 10.5px; white-space: nowrap; }
  .contact { position: absolute; display: flex; align-items: center; gap: 8px; font-size: 13.5px; white-space: nowrap; }
  .contact svg { width: 16px; height: 14px; flex: none; }

  /* card A */
  .card--front-a .light-band {
    position: absolute; left: 22px; top: 22px; width: 540px; height: 84px;
    background: linear-gradient(90deg, var(--card-navy) 0%, var(--band-mid) 30%, var(--band-light) 50%, var(--band-mid) 70%, var(--card-navy) 100%);
  }
  .card--front-a .wordmark { left: 22px; top: 22px; width: 540px; height: 84px; font-size: 15px; }
  .card--front-a .holder-name { left: 39px; top: 181px; font-size: 18px; }
  .card--front-a .divider { position: absolute; left: 250px; top: 150px; width: 3px; height: 98px; background: var(--ink-white); }

  /* card B */
  .card--front-b .light-band {
    position: absolute; left: 486px; top: 0; width: 95px; height: 327px;
    background: linear-gradient(90deg, var(--band-deep) 0%, var(--band-light) 45%, var(--band-mid) 80%, var(--band-deep) 100%);
  }
  .card--front-b .wordmark { left: 486px; top: 140px; width: 95px; font-size: 11px; gap: 4px; letter-spacing: 0; }
  .card--front-b .wordmark__dot { width: 10px; height: 10px; }
  .card--front-b .holder-name { left: 19px; top: 37px; font-size: 21px; }
  .card--front-b .licence-intro,
  .card--front-b .service { right: 133px; text-align: right; }

  /* back */
  .back-pattern {
    position: absolute; inset: 0;
    background: radial-gradient(ellipse at 50% 45%, var(--pattern-a) 0%, var(--pattern-b) 75%);
  }
  .card--back .wordmark {
    left: 0; top: 0; width: 627px; height: 350px;
    flex-direction: column; gap: 14px;
    color: var(--silver); font-size: 38px; letter-spacing: 3px; text-align: center; line-height: 1.1;
  }
  .card--back .wordmark__dot { width: 96px; height: 96px; background: var(--silver); }
</style>
</head>
<body>

<svg width="0" height="0" style="position:absolute" aria-hidden="true">
  <defs>
    <symbol id="icon-house" viewBox="0 0 16 14"><path d="M1 7 L8 1 L15 7 M3 6 V13 H13 V6" fill="none" stroke="#fff" stroke-width="1.6"/><rect x="6.5" y="8.5" width="3" height="4.5" fill="#fff"/></symbol>
    <symbol id="icon-mail" viewBox="0 0 16 14"><rect x="1" y="2" width="14" height="10" rx="1" fill="#fff"/><path d="M1 3 L8 8 L15 3" fill="none" stroke="#07101f" stroke-width="1.2"/></symbol>
    <symbol id="icon-web" viewBox="0 0 16 14"><circle cx="8" cy="7" r="6" fill="none" stroke="#fff" stroke-width="1.6"/><path d="M5 5 L6.5 10 L8 6.5 L9.5 10 L11 5" fill="none" stroke="#fff" stroke-width="1.2"/></symbol>
    <symbol id="icon-phone" viewBox="0 0 16 14"><path d="M1 5 Q8 0 15 5 L13 7 L11 5.5 L5 5.5 L3 7 Z" fill="#fff"/><rect x="4" y="7" width="8" height="6" rx="1" fill="#fff"/></symbol>
    <symbol id="icon-fax" viewBox="0 0 16 14"><rect x="4" y="1" width="8" height="5" fill="none" stroke="#fff" stroke-width="1.2"/><rect x="1" y="6" width="14" height="7" rx="1" fill="#fff"/></symbol>
  </defs>
</svg>

<section class="card card--front-a" aria-label="Business card, information side, horizontal layout">
  <div class="light-band"></div>
  <div class="wordmark"><span class="wordmark__dot"></span>TARROWIN CONSTRUCTION</div>
  <p class="holder-name">Your Name Here</p>
  <div class="divider"></div>
  <p class="contact" style="left:300px;top:143px"><svg><use href="#icon-house"/></svg>PO Box 8641 Kellsmoor QLD 4019</p>
  <p class="contact" style="left:300px;top:168px"><svg><use href="#icon-mail"/></svg>person@tarrowinconstruction.example.au</p>
  <p class="contact" style="left:300px;top:193px"><svg><use href="#icon-web"/></svg>www.tarrowinconstruction.example.au</p>
  <p class="contact" style="left:300px;top:218px"><svg><use href="#icon-phone"/></svg>333 481 602</p>
  <p class="contact" style="left:300px;top:241px"><svg><use href="#icon-fax"/></svg>333 481 715</p>
  <p class="licence-intro" style="left:180px;top:266px">Licensed buiders specialising in</p>
  <p class="service" style="left:114px;top:282px">Bathrooms</p>
  <p class="service" style="left:240px;top:282px">Kitchens</p>
  <p class="service" style="left:334px;top:282px">Comercial Interiors</p>
  <p class="footnote" style="left:14px">ABN: 62407938215</p>
  <p class="footnote" style="right:14px">BSA license: xxx-xxxx</p>
</section>

<section class="card card--front-b" aria-label="Business card, information side, band layout">
  <div class="light-band"></div>
  <div class="wordmark"><span class="wordmark__dot"></span>TARROWIN</div>
  <p class="holder-name">Your Name Here</p>
  <p class="licence-intro" style="top:125px">Licensed buiders specialising in</p>
  <p class="service" style="top:142px">Bathrooms</p>
  <p class="service" style="top:160px">Kitchens</p>
  <p class="service" style="top:178px">Comercial Interiors</p>
  <p class="contact" style="left:10px;top:259px;font-size:12px"><svg><use href="#icon-house"/></svg>PO Box 8641 Kellsmoor QLD 4019</p>
  <p class="contact" style="left:245px;top:259px;font-size:12px"><svg><use href="#icon-phone"/></svg>333 481 602</p>
  <p class="contact" style="left:355px;top:259px;font-size:12px"><svg><use href="#icon-fax"/></svg>333 481 715</p>
  <p class="contact" style="left:10px;top:277px;font-size:12px"><svg><use href="#icon-web"/></svg>www.tarrowinconstruction.example.au</p>
  <p class="contact" style="left:245px;top:277px;font-size:12px"><svg><use href="#icon-mail"/></svg>person@tarrowinconstruction.example.au</p>
  <p class="footnote" style="left:14px">ABN: 62407938215</p>
  <p class="footnote" style="right:110px">BSA license: xxx-xxxx</p>
</section>

<section class="card card--back" aria-label="Business card, logo side">
  <div class="back-pattern" role="img" aria-label="Dark blue interlocking mosaic pattern behind the company name"></div>
  <div class="wordmark"><span class="wordmark__dot"></span>TARROWIN<br>CONSTRUCTION</div>
</section>

</body>
</html>
```